Retirement maintenance and reinstatment brochure

We are looking for a capability statement/brochure outlining our skills and capabilities for maintenance, reinstatement and refurbishment work specific to the requirements of retirement villages in Australia

We are a new company, however our people have significant experience working in this industry

Target Market(s)

Retirement living facilities, aged care facilities, hospitals

Industry/Entity Type

Building

Colors

Designer to choose colors to be used in the design.

Requirements
Must have
• Not alot of wording. Stock images of building refurbishment to retirement living and aged care (carpenters, painters etc)
Nice to have
• 1-2 pages only
Should not have
• alot of meaningless writing

```html
<!DOCTYPE html>
<html lang="en">
<head>
<meta charset="UTF-8">
<title>Coastline Care Maintenance Services – Flyer</title>
<link rel="stylesheet" href="https://fonts.googleapis.com/css2?family=Open+Sans:wght@400;600;700;800&family=Oswald:wght@500&display=swap">
<style>
  :root {
    --navy: #1c3f7c;
    --red: #e11f2b;
    --ink: #1e1e1e;
    --paper: #ffffff;
    --mist: #eef2f8;
  }
  * { margin: 0; padding: 0; box-sizing: border-box; }
  html, body { width: 960px; height: 1200px; overflow: hidden; background: var(--paper); }
  body { font-family: "Open Sans", Arial, sans-serif; color: var(--ink); }

  .flyer { position: relative; width: 960px; height: 1200px; overflow: hidden;
    background: linear-gradient(180deg, var(--paper) 0%, var(--mist) 55%, var(--paper) 85%); }

  .hero-photo { position: absolute; left: 0; top: 0; width: 600px; height: 520px;
    background: linear-gradient(135deg, #cfd9e6 0%, #e9c9d6 45%, #d8c7b8 75%, rgba(255,255,255,0) 100%);
    -webkit-mask-image: linear-gradient(90deg, #000 70%, transparent 100%), linear-gradient(180deg, #000 75%, transparent 100%);
    -webkit-mask-composite: source-in; mask-composite: intersect; }

  .brand { position: absolute; right: 60px; top: 70px; display: flex; align-items: center; gap: 14px; }
  .brand-dot { width: 56px; height: 56px; border-radius: 50%; background: var(--navy); }
  .brand-name { font-family: "Oswald", "Arial Narrow", sans-serif; font-weight: 500; color: var(--red);
    font-size: 30px; line-height: 1.05; text-transform: uppercase; letter-spacing: .5px; }

  .intro { position: absolute; right: 60px; top: 160px; width: 420px; text-align: right; }
  .intro-lead { font-weight: 800; font-size: 42px; color: var(--red); line-height: 48px; }
  .intro-line { font-size: 20px; line-height: 26px; }
  .intro-line.strong { font-weight: 700; color: var(--navy); }
  .intro-line.accent { color: var(--red); }
  .intro-line.plain { color: var(--ink); }
  .intro-gap { height: 10px; }
  .intro-line.accent.strong { color: var(--red); }

  .team { position: absolute; left: 0; top: 0; width: 960px; height: 1200px; pointer-events: none; }
  .trade-photo { position: absolute; border-radius: 50%; border-style: solid; border-width: 10px; }
  .trade-photo.red { border-color: var(--red); }
  .trade-photo.blue { border-color: var(--navy); }

  .badge { position: absolute; left: 752px; top: 660px; width: 122px; height: 122px; border-radius: 50%;
    background: radial-gradient(circle, #f4f4f4 0 55%, #b9bcc2 56% 100%); }
  .badge-ribbon { position: absolute; left: -12px; top: 62px; width: 146px; height: 34px; background: var(--red);
    color: #fff; font-weight: 800; font-size: 18px; text-align: center; line-height: 34px; transform: rotate(-8deg); }
  .badge-hours { position: absolute; width: 100%; top: 22px; text-align: center; font-weight: 800; font-size: 30px; color: var(--red); }

  .trades { position: absolute; left: 84px; top: 762px; }
  .trades-kicker { font-size: 22px; color: var(--navy); line-height: 1.1; }
  .trades-title { font-weight: 800; font-size: 38px; color: var(--red); line-height: 1.1; }
  .trades-rule { width: 180px; height: 2px; background: var(--navy); margin: 6px 0 10px; opacity: .6; }
  .trades-list { list-style: none; }
  .trades-list li { font-size: 20px; font-weight: 600; line-height: 29px; display: flex; align-items: center; gap: 12px; }
  .trades-list li::before { content: ""; width: 11px; height: 11px; border-radius: 50%;
    border: 3px solid var(--navy); border-right-color: var(--red); flex: none; }

  .about { position: absolute; left: 493px; top: 800px; width: 420px; font-size: 14.5px; line-height: 1.38; }
  .promise { position: absolute; left: 493px; top: 940px; width: 420px; font-weight: 800; font-size: 19px;
    line-height: 26px; color: var(--navy); }
  .promise .hot { color: var(--red); }

  .footer-band { position: absolute; left: 0; bottom: 0; width: 960px; height: 150px; }
  .footer-web { position: absolute; left: 68px; bottom: 30px; color: #fff; font-size: 22px; display: flex; align-items: center; gap: 10px; }
  .footer-call { position: absolute; right: 60px; bottom: 20px; color: #fff; text-align: right; }
  .call-label { font-size: 30px; font-weight: 600; line-height: 1.1; }
  .call-number { font-size: 42px; font-weight: 800; display: flex; align-items: center; gap: 14px; line-height: 1.15; }
</style>
</head>
<body>
<main class="flyer">
  <div class="hero-photo" role="img" aria-label="Photo of a smiling older woman at home making a phone call"></div>

  <header class="brand">
    <span class="brand-dot"></span>
    <span class="brand-name">Coastline Care<br>Maintenance Services</span>
  </header>

  <section class="intro">
    <p class="intro-lead">WE ARE A</p>
    <p class="intro-line strong">COMMERCIAL BUILDING AND<br>MAINTENANCE COMPANY</p>
    <p class="intro-line plain">ESTABLISHED AND LOCATED ON</p>
    <p class="intro-line accent">THE SUNSHINE COAST IN QLD.</p>
    <div class="intro-gap"></div>
    <p class="intro-line strong">WE ARE</p>
    <p class="intro-line accent strong">LICENSED AND INSURED</p>
    <p class="intro-line plain">and have a full workplace<br>health and safety<br>compliance system.</p>
  </section>

  <div class="team">
    <div class="trade-photo red" style="left:80px;top:478px;width:280px;height:280px;background:linear-gradient(160deg,#bcd9f4,#6fa6dc);" role="img" aria-label="Photo of a builder in a hard hat writing on a clipboard"></div>
    <div class="trade-photo blue" style="left:387px;top:410px;width:250px;height:250px;background:linear-gradient(160deg,#e98d93,#f1c4c2);" role="img" aria-label="Photo of a painter in overalls holding a paint roller"></div>
    <div class="trade-photo blue" style="left:645px;top:478px;width:185px;height:185px;background:linear-gradient(160deg,#8f98a6,#d6dde6);" role="img" aria-label="Photo of a plumber working on pipes"></div>
    <div class="trade-photo blue" style="left:303px;top:600px;width:168px;height:168px;background:linear-gradient(160deg,#c9c3bb,#9c948b);" role="img" aria-label="Photo of a hand plastering a wall with a trowel"></div>
    <div class="trade-photo red" style="left:466px;top:578px;width:198px;height:198px;background:linear-gradient(160deg,#8b7a68,#4f5a6e);" role="img" aria-label="Photo of a carpenter in an apron in a workshop"></div>
  </div>

  <div class="badge">
    <div class="badge-hours">24h</div>
    <div class="badge-ribbon">SERVICE</div>
  </div>

  <section class="trades">
    <p class="trades-kicker">TRADES WE</p>
    <h2 class="trades-title">SPECIALISE IN:</h2>
    <div class="trades-rule"></div>
    <ul class="trades-list">
      <li>Painting and building cleaning</li>
      <li>Carpentry and minor repairs</li>
      <li>Plastering and rendering</li>
      <li>Carpet and floor laying</li>
      <li>Electrical</li>
      <li>Plumbing</li>
      <li>Air Conditioning upgrades</li>
    </ul>
  </section>

  <p class="about">We have expertise in retirement living and aged care maintenance works such as cleaning and painting programs, reinstatement works including painting and carpet replacement as well as major refurbishment or upgrade works including kitchen and bathroom works, electrical and air conditioning upgrade works.</p>

  <p class="promise">WE HAVE THE ABILITY TO<br>REACT QUICKLY AND <span class="hot">COMPLETE</span><br><span class="hot">WORKS</span> WITH AS LITTLE AS<br><span class="hot">24 HOURS NOTICE.</span></p>

  <svg class="footer-band" viewBox="0 0 960 150" aria-hidden="true">
    <path d="M0 18 Q480 100 960 22" fill="none" stroke="var(--red)" stroke-width="2"/>
    <path d="M0 30 Q480 110 960 34 L960 150 L0 150 Z" fill="var(--navy)"/>
  </svg>

  <div class="footer-web">
    <svg width="20" height="20" viewBox="0 0 20 20" aria-hidden="true"><g fill="none" stroke="#fff" stroke-width="1.6"><circle cx="10" cy="10" r="8.5"/><ellipse cx="10" cy="10" rx="3.8" ry="8.5"/><path d="M1.5 10h17M3 5.5h14M3 14.5h14"/></g></svg>
    <span>www.yourweb.com</span>
  </div>

  <div class="footer-call">
    <p class="call-label">CALL US</p>
    <p class="call-number">
      <svg width="34" height="34" viewBox="0 0 36 36" aria-hidden="true"><circle cx="18" cy="18" r="16" fill="none" stroke="#fff" stroke-width="2.5"/><path d="M12 9.5l3.5-.5 2 5-2.3 1.6a11 11 0 0 0 5.2 5.2l1.6-2.3 5 2-.5 3.5c-7.5.8-15.3-7-14.5-14.5z" fill="#fff"/></svg>
      <span>0123 456 789</span>
    </p>
  </div>
</main>
</body>
</html>
```